Toddler Music Class Bussiness Needs Web Design

We are a small start up called "PebbleBoppers" providing music classes to kids from 6 months to 3 years of age. Kids are instructor led and learn to play a variety of instruments (e.g. drums, tambourines, ukulele's, castanets, etc..), develop coordination and rhythm, and stimulate mental development while having a blast of a time along with other kids and their parents.
The website design needs to be clever, have clean lines, simple modern font, original, fun and colourful and professional. It will need to look good when viewed across different devices and be able to scale well when resized.
This website needs to convey the message that the classes will be enjoyed by parents and children, be safe and contribute to the development of their children.
We have a logo that needs to be incorporated into the design and lead the approach. There will be a number of web pages illustrated in the site map accompanied with this project. The winning bid will have a design that represents a number of pages of the website e.g. 4/5 of the pages

****** commercial in confidence ******
Updates

Reason: Hi Designers, appreciate the design submissions thus far. We have decided to extend tge deadline due to requests from designers :)

Just wanted to say thanks for the designs sent through, there are a few good ones (:

In general we are looking for a little more of a playful approach and have included a few variations on the logos to encourage different design approaches.

Feel free to have a play!!

Target Market(s)

Parents in Australia (multicultural) aged 25 to 45

Industry/Entity Type

Learn

Requirements
Must have
• The website design needs to be clever, have clean lines, simple modern font, original, fun and colourful and professional. It will need to look good when viewed across different devices and be able to scale well when resized.
We have a logo that needs to be incorporated into the design and lead the approach.

```html
<!DOCTYPE html>
<html lang="en">
<head>
<meta charset="utf-8">
<title>PebbleBoppers – Music Classes for Little Ones</title>
<link href="https://fonts.googleapis.com/css2?family=Courgette&family=Roboto:wght@400;500;700&display=swap" rel="stylesheet">
<style>
:root{
  --purple:#8f3d98;
  --blue:#1565b3;
  --green:#29a336;
  --amber:#ef9a0b;
  --sky:#0bb2e4;
  --coral:#e8694a;
  --sage:#76b86c;
  --pink:#e8164e;
  --orange:#f47420;
  --lime:#6ab516;
  --navy:#13203a;
  --title:#1a5fa8;
  --text:#4a4a4a;
  --red:#d8203e;
}
*{box-sizing:border-box;margin:0;padding:0}
html,body{width:1071px;height:1200px;overflow:hidden}
body{
  position:relative;
  font-family:"Roboto",Arial,sans-serif;
  color:var(--text);
  background:
    radial-gradient(circle at 6% 40%,rgba(255,255,255,.75) 0 40px,transparent 70px),
    radial-gradient(circle at 95% 30%,rgba(255,255,255,.7) 0 40px,transparent 70px),
    radial-gradient(circle at 5% 80%,rgba(255,255,255,.7) 0 35px,transparent 65px),
    radial-gradient(circle at 96% 75%,rgba(255,255,255,.7) 0 40px,transparent 70px),
    linear-gradient(180deg,#e6e7ec,#dcdde3 50%,#e3e4e9);
}
.abs{position:absolute}
.top-strip{left:0;top:0;width:1071px;height:4px;background:var(--purple)}
.brand{left:178px;top:34px;display:flex;align-items:center;gap:10px;font-weight:700;font-size:30px;color:var(--blue);letter-spacing:.5px}
.brand-dot{width:26px;height:26px;border-radius:50%;background:var(--pink)}
.join{left:813px;top:24px;width:79px;height:20px;background:var(--sage);color:#fff;font-size:9px;display:flex;align-items:center;justify-content:center}
.search{left:635px;top:61px;width:134px;height:19px;border:1px solid #c9c9c9;background:#fff;font-size:8px;color:#999;padding:4px 7px}
.search-btn{left:769px;top:61px;width:19px;height:19px;background:#3a3a3a}
.social-top{left:790px;top:61px;display:flex;gap:2px}
.social-top span{width:19px;height:19px}
.nav{left:178px;top:105px;width:714px;height:45px;display:flex}
.nav a{flex:1;display:flex;align-items:center;justify-content:center;color:#fff;font-size:10.5px;text-decoration:none}
.slider{left:178px;top:159px;width:715px;height:335px;border:4px solid var(--coral);background:#fff;overflow:hidden}
.slide-photo{position:absolute;inset:0;background:
  radial-gradient(ellipse 110px 130px at 24% 55%,#f6c52a 0,rgba(246,197,42,.55) 55%,transparent 100%),
  radial-gradient(ellipse 110px 130px at 52% 55%,#7ed23a 0,rgba(126,210,58,.55) 55%,transparent 100%),
  radial-gradient(ellipse 80px 40px at 52% 88%,rgba(70,100,150,.55) 0,transparent 100%),
  radial-gradient(ellipse 110px 130px at 82% 58%,#f1e4d8 0,rgba(230,210,195,.6) 55%,transparent 100%),
  radial-gradient(ellipse 60px 20px at 80% 88%,rgba(240,120,40,.6) 0,transparent 100%),
  linear-gradient(180deg,#fff 0%,#f6f6f6 75%,#ececec 100%)}
.slide-arrow{width:30px;height:30px;border-radius:50%;background:rgba(120,120,120,.6)}
.dots{left:474px;top:468px;width:123px;height:22px;background:var(--coral);display:flex;align-items:center;justify-content:center;gap:6px}
.dots i{width:8px;height:8px;border-radius:50%;background:#f3c0b0}
.dots i:first-child{background:#fff}
.script{font-family:"Courgette",cursive;color:var(--title);font-weight:400}
.welcome-title{left:0;width:1071px;top:512px;text-align:center;font-size:19px}
.welcome-text{left:160px;top:545px;width:750px;text-align:center;font-size:8.4px;line-height:17px;color:#555;white-space:nowrap}
.read-btn{left:479px;top:624px;width:113px;height:26px;background:var(--purple);color:#fff;font-size:9.5px;font-style:italic;display:flex;align-items:center;justify-content:center}
.section-title{font-size:18px}
.cards{left:178px;top:718px;display:flex;gap:8px}
.card{position:relative;width:233px;height:163px;overflow:hidden}
.card-photo{position:absolute;left:0;top:0;width:100%;height:135px}
.card-corner{position:absolute;right:0;top:0;width:42px;height:42px}
.card-label{position:absolute;left:0;bottom:0;width:100%;height:28px;color:#fff;font-size:12px;font-weight:500;display:flex;align-items:center;justify-content:space-between;padding:0 12px}
.plus{width:14px;height:14px}
.small-text{font-size:8px;line-height:17px;color:#555;white-space:nowrap}
.pager{font-size:9px;color:#333;letter-spacing:2px}
.video{display:flex;gap:12px}
.video-thumb{width:67px;height:63px;border:1px solid #fff}
.video h4{font-size:9px;font-weight:500;color:#555;margin-top:6px}
.video p{font-size:8px;line-height:10px;color:#555;margin-top:5px;width:170px}
.video a{display:block;font-size:8px;color:var(--red);font-weight:500;margin-top:5px;text-decoration:none}
.quote{left:680px;top:1009px;width:210px;text-align:center;font-size:9.5px;line-height:17px;color:#555;white-space:nowrap}
.footer{left:0;top:1142px;width:1071px;height:58px;background:var(--navy)}
.copyright{left:178px;top:1166px;font-size:8.5px;color:#fff;font-weight:500}
.social-foot{left:758px;top:1159px;display:flex;gap:14px}
.social-foot span{width:22px;height:22px}
</style>
</head>
<body>
<div class="abs top-strip"></div>

<header>
  <div class="abs brand"><span class="brand-dot"></span>PebbleBoppers</div>
  <div class="abs join">Join Us</div>
  <div class="abs search">Search</div>
  <div class="abs search-btn">
    <svg width="19" height="19" viewBox="0 0 19 19"><circle cx="8.5" cy="8.5" r="3.5" fill="none" stroke="#fff" stroke-width="1.5"/><line x1="11" y1="11" x2="14" y2="14" stroke="#fff" stroke-width="1.5"/></svg>
  </div>
  <div class="abs social-top" aria-label="Social links">
    <span style="background:#2aa9e0"></span>
    <span style="background:#3b5998"></span>
    <span style="background:#e84c8a"></span>
    <span style="background:#0077b5"></span>
    <span style="background:#f7a531"></span>
  </div>
  <nav class="abs nav">
    <a style="background:var(--blue)">Home</a>
    <a style="background:var(--green)">About us</a>
    <a style="background:var(--amber)">Enrol</a>
    <a style="background:var(--sky)">Classes</a>
    <a style="background:var(--coral)">Contact Us</a>
    <a style="background:var(--sage)">Merchandise</a>
  </nav>
</header>

<section class="abs slider">
  <div class="slide-photo" role="img" aria-label="Three babies in yellow, green and white tops playing with maracas, a tambourine and a toy xylophone"></div>
  <div class="abs slide-arrow" style="left:25px;top:146px">
    <svg width="30" height="30" viewBox="0 0 30 30"><polyline points="17,9 11,15 17,21" fill="none" stroke="#fff" stroke-width="2.5"/></svg>
  </div>
  <div class="abs slide-arrow" style="left:652px;top:146px">
    <svg width="30" height="30" viewBox="0 0 30 30"><polyline points="13,9 19,15 13,21" fill="none" stroke="#fff" stroke-width="2.5"/></svg>
  </div>
</section>
<div class="abs dots"><i></i><i></i><i></i><i></i><i></i></div>

<section>
  <h1 class="abs script welcome-title">Welcome To Our Website</h1>
  <p class="abs welcome-text">Lorem ipsum dolor sit amet, consectetuer adipiscing elit, sed diam nonummy nibh euismod tincidunt ut laoreet dolore magna aliquam erat volutpat. Lorem ipsum dolor sit amet, consec-<br>tetuer adipiscing elit, sed diam nonummy nibh euismod tincidunt ut laoreet dolore magna aliquam erat volutpat. Lorem ipsum dolor sit amet, consectetuer adipiscing elit, sed diam<br>nonummy nibh euismod tincidunt ut laoreet dolore magna aliquam erat volutpat. Lorem ipsum dolor sit amet, consectetuer adipiscing elit, sed diam nonummy nibh euismod tincidunt ut<br>laoreet dolore magna aliquam erat volutpat.</p>
  <div class="abs read-btn">Read More +</div>
</section>

<section>
  <h2 class="abs script section-title" style="left:178px;top:679px">Instruments</h2>
  <svg class="abs" style="left:866px;top:686px" width="24" height="12" viewBox="0 0 24 12"><polyline points="8,1 3,6 8,11" fill="none" stroke="#222" stroke-width="2.2"/><polyline points="15,1 20,6 15,11" fill="none" stroke="#e8165e" stroke-width="2.2"/></svg>
  <div class="abs cards">
    <div class="card">
      <div class="card-photo" role="img" aria-label="Toddler playing a red drum kit" style="background:linear-gradient(160deg,#efe7df,#c9a99a 60%,#b8282c)"></div>
      <svg class="card-corner" viewBox="0 0 42 42"><path d="M0 0H42V42C42 18 24 0 0 0Z" fill="var(--pink)"/></svg>
      <div class="card-label" style="background:var(--pink)">Drums<svg class="plus" viewBox="0 0 14 14"><circle cx="7" cy="7" r="7" fill="#fff"/><path d="M7 3.5v7M3.5 7h7" stroke="var(--pink)" stroke-width="1.8"/></svg></div>
    </div>
    <div class="card">
      <div class="card-photo" role="img" aria-label="Group of children in red shirts playing tambourines" style="background:linear-gradient(170deg,#d8b59a,#c04a3a 55%,#a8342c)"></div>
      <svg class="card-corner" viewBox="0 0 42 42"><path d="M0 0H42V42C42 18 24 0 0 0Z" fill="var(--orange)"/></svg>
      <div class="card-label" style="background:var(--orange)">Tambourines<svg class="plus" viewBox="0 0 14 14"><circle cx="7" cy="7" r="7" fill="#fff"/><path d="M7 3.5v7M3.5 7h7" stroke="var(--orange)" stroke-width="1.8"/></svg></div>
    </div>
    <div class="card">
      <div class="card-photo" role="img" aria-label="Hands strumming a ukulele" style="background:linear-gradient(135deg,#6e4a22,#c98a3a 50%,#e0b070)"></div>
      <svg class="card-corner" viewBox="0 0 42 42"><path d="M0 0H42V42C42 18 24 0 0 0Z" fill="var(--lime)"/></svg>
      <div class="card-label" style="background:var(--lime)">Ukulele's<svg class="plus" viewBox="0 0 14 14"><circle cx="7" cy="7" r="7" fill="#fff"/><path d="M7 3.5v7M3.5 7h7" stroke="var(--lime)" stroke-width="1.8"/></svg></div>
    </div>
  </div>
</section>

<section>
  <h2 class="abs script section-title" style="left:178px;top:912px">Classes</h2>
  <div class="abs pager" style="left:366px;top:917px">‹›</div>
  <div class="abs" role="img" aria-label="Row of colourful ukuleles on display" style="left:178px;top:942px;width:200px;height:83px;background:linear-gradient(90deg,#5a6070,#d88a4a 30%,#d060a0 55%,#4aa0d0 80%,#5a6070)"></div>
  <p class="abs small-text" style="left:178px;top:1050px">The management consulting firm the world's busi-<br>ness leaders come to when they want</p>
  <div class="abs" style="left:178px;top:1086px;font-size:8px;color:#222">Read More +</div>
</section>

<section>
  <h2 class="abs script section-title" style="left:394px;top:912px">Training Videos</h2>
  <div class="abs" style="left:610px;top:919px;font-size:8.5px;color:#222">View more +</div>
  <div class="abs video" style="left:394px;top:942px">
    <div class="video-thumb" role="img" aria-label="Child playing a small guitar" style="background:linear-gradient(135deg,#4a5a7a,#a88a6a)"></div>
    <div><h4>SUSPENDISSE MATTIS TELI</h4><p>Suspendisse mattis tellus vel augue mollis ultrices suspends</p><a>Read More +</a></div>
  </div>
  <div class="abs video" style="left:394px;top:1018px">
    <div class="video-thumb" role="img" aria-label="Close-up of a yellow guitar" style="background:linear-gradient(135deg,#3a2a1a,#e0a020 60%,#c03020)"></div>
    <div><h4>SUSPENDISSE MATTIS TELI</h4><p>Suspendisse mattis tellus vel augue mollis ultrices suspends</p><a>Read More +</a></div>
  </div>
</section>

<section>
  <h2 class="abs script section-title" style="left:690px;top:909px">Parents say's</h2>
  <div class="abs pager" style="left:880px;top:914px">‹›</div>
  <div class="abs" role="img" aria-label="Portrait of a smiling parent" style="left:755px;top:944px;width:60px;height:60px;border-radius:50%;background:radial-gradient(circle,#d8b090,#8a6a50);border:2px solid #fff"></div>
  <p class="abs quote">Donec sed odio dui. Nullam id dolor id<br>nibh ultricies vehicula ut id elit. Sollicitu-<br>din Lorem Egestas Dapibus.</p>
  <div class="abs" style="left:801px;top:1068px;font-size:10px;color:#777">“</div>
  <div class="abs" style="left:790px;top:1084px;width:101px;text-align:right;font-size:9.5px;color:#222">Mr.Tom, Manager</div>
</section>

<footer>
  <div class="abs footer"></div>
  <div class="abs copyright">COPYRIGHT © 2014 PebbleBoppers, ALL RIGHTS RESERVED.</div>
  <div class="abs social-foot" aria-label="Social links">
    <span style="background:#3b5998"></span>
    <span style="background:#5a7fa8"></span>
    <span style="background:#2aa9e0"></span>
    <span style="background:#d62e2e"></span>
  </div>
</footer>
</body>
</html>
```